Ad design for a macarons brand

We are a dessert brand with one product line: macarons. Our products delight. Every bite is a dream!

We are launching a new product and would like to lunch a small tactical campaign for the product to boost sales.

The new macron is mango ganache and the middle a mix of sour mango and yuzu (https://www.plumvarell.com/about-the-fruit-584302).

Here are some images we took of the new macaron
https://www.fennlocker.com/sh/qrtwpzhkvbmls/AAFJtRWD-nxPlkhQZ7CeW4DLp?dl=0

I attach the brand guideline document.

Required sizes

1080 x 1350
1080 x 1920

```html
<!DOCTYPE html>
<html lang="en">
<head>
<meta charset="utf-8">
<title>Merls — New Macaron</title>
<link href="https://fonts.googleapis.com/css2?family=Playfair+Display:wght@400&display=swap" rel="stylesheet">
<style>
  :root {
    --saffron: #fdc00f;
    --lemon: #f8e44c;
    --white: #ffffff;
    --mango-light: #f2b24a;
    --mango-deep: #e08a2c;
  }
  html, body {
    margin: 0;
    padding: 0;
    overflow: hidden;
    background: var(--saffron);
  }
  .ad {
    position: relative;
    width: 675px;
    height: 1200px;
    background: var(--saffron);
    overflow: hidden;
  }
  .ad__pattern {
    position: absolute;
    inset: 0;
  }
  .ad__pattern text {
    font-family: "Playfair Display", serif;
    font-size: 126px;
    fill: var(--white);
  }
  .ad__panel {
    position: absolute;
    left: 141px;
    top: 251px;
    width: 393px;
    height: 699px;
    background: var(--lemon);
  }
  .ad__product {
    position: absolute;
    left: 65px;
    top: 210px;
    width: 267px;
    height: 217px;
    border-radius: 50% / 46%;
    background: radial-gradient(ellipse at 45% 35%, var(--mango-light), var(--mango-deep));
  }
  .brand-name {
    position: absolute;
    left: 0;
    right: 0;
    top: 575px;
    margin: 0;
    text-align: center;
    color: var(--white);
    font-family: "Playfair Display", serif;
    font-weight: 400;
    font-size: 56px;
    line-height: 1;
    letter-spacing: 1px;
  }
</style>
</head>
<body>
<main class="ad">
  <svg class="ad__pattern" width="675" height="1200" viewBox="0 0 675 1200" aria-hidden="true">
    <g class="pattern-left">
      <text x="34" y="130" textLength="290" lengthAdjust="spacingAndGlyphs">NEW</text>
      <text x="34" y="244" textLength="290" lengthAdjust="spacingAndGlyphs">NEW</text>
      <text x="34" y="358" textLength="290" lengthAdjust="spacingAndGlyphs">NEW</text>
      <text x="34" y="472" textLength="290" lengthAdjust="spacingAndGlyphs">NEW</text>
      <text x="34" y="586" textLength="290" lengthAdjust="spacingAndGlyphs">NEW</text>
      <text x="34" y="700" textLength="290" lengthAdjust="spacingAndGlyphs">NEW</text>
      <text x="34" y="814" textLength="290" lengthAdjust="spacingAndGlyphs">NEW</text>
      <text x="34" y="928" textLength="290" lengthAdjust="spacingAndGlyphs">NEW</text>
      <text x="34" y="1042" textLength="290" lengthAdjust="spacingAndGlyphs">NEW</text>
      <text x="34" y="1156" textLength="290" lengthAdjust="spacingAndGlyphs">NEW</text>
    </g>
    <g class="pattern-right">
      <text x="352" y="130" textLength="292" lengthAdjust="spacingAndGlyphs">NEW</text>
      <text x="352" y="244" textLength="292" lengthAdjust="spacingAndGlyphs">NEW</text>
      <text x="352" y="358" textLength="292" lengthAdjust="spacingAndGlyphs">NEW</text>
      <text x="352" y="472" textLength="292" lengthAdjust="spacingAndGlyphs">NEW</text>
      <text x="352" y="586" textLength="292" lengthAdjust="spacingAndGlyphs">NEW</text>
      <text x="352" y="700" textLength="292" lengthAdjust="spacingAndGlyphs">NEW</text>
      <text x="352" y="814" textLength="292" lengthAdjust="spacingAndGlyphs">NEW</text>
      <text x="352" y="928" textLength="292" lengthAdjust="spacingAndGlyphs">NEW</text>
      <text x="352" y="1042" textLength="292" lengthAdjust="spacingAndGlyphs">NEW</text>
      <text x="352" y="1156" textLength="292" lengthAdjust="spacingAndGlyphs">NEW</text>
    </g>
  </svg>

  <section class="ad__panel">
    <div class="ad__product" role="img" aria-label="Photo of the new mango and yuzu macaron with golden shells and mango filling"></div>
    <p class="brand-name">Merls</p>
  </section>
</main>
</body>
</html>
```